Crest Automotive Reconditioning Business Card

We need a professional business card that features our logo, a picture of the employee, and a brief list of our services.
I've attached a logo, and will attach photos at a later date.
The four services that need to be listed are Bumper repair and repainting, road rash repair, clear coat scratch repair, and automotive touch-up.
Target Market(s)
30 - 40 year male general managers of automobile dealerships. They are used to seeing every vendor gimmick under the sun. This brochure needs to impress with its simplicity and honesty.
Industry/Entity Type
Automotive
Look and feel
Each slider illustrates characteristics of the customer's brand and the style your logo design should communicate.

```html
<!DOCTYPE html>
<html lang="en">
<head>
<meta charset="utf-8">
<title>Crest Automotive Reconditioning – Business Card</title>
<link href="https://fonts.googleapis.com/css2?family=Open+Sans:wght@400;600;700&display=swap" rel="stylesheet">
<style>
  :root {
    --orange: #ee5a24;
    --orange-deep: #c83a0e;
    --orange-bright: #f26a2e;
    --charcoal: #2d2d2f;
    --charcoal-deep: #232325;
    --ink: #333335;
    --white: #ffffff;
    --backdrop: #8a8a8a;
    --rule: #8c8c8c;
  }
  * { margin: 0; padding: 0; box-sizing: border-box; }
  html, body { width: 1200px; height: 900px; overflow: hidden; }
  body {
    background: var(--backdrop);
    font-family: "Open Sans", Arial, sans-serif;
    position: relative;
  }

  /* ---------- Front of card ---------- */
  .card-front {
    position: absolute;
    left: 66px; top: 45px;
    width: 777px; height: 444px;
    overflow: hidden;
    background: var(--white);
  }
  .card-front .bands { position: absolute; inset: 0; }
  .front-brand {
    position: absolute;
    left: 0; right: 0; top: 200px;
    text-align: center;
    color: var(--ink);
    font-weight: 700;
  }
  .front-brand .brand-name {
    display: block;
    font-size: 92px;
    line-height: 1;
    letter-spacing: 6px;
  }
  .front-brand .brand-tagline {
    display: block;
    font-size: 21px;
    letter-spacing: 1px;
    margin-top: 10px;
    text-transform: uppercase;
  }

  /* ---------- Back of card ---------- */
  .card-back {
    position: absolute;
    left: 487px; top: 502px;
    width: 598px; height: 358px;
    overflow: hidden;
    background: var(--charcoal);
  }
  .card-back .panels { position: absolute; inset: 0; }
  .back-brand {
    position: absolute;
    left: 18px; top: 140px;
    width: 190px;
    text-align: center;
    color: var(--white);
    font-weight: 700;
  }
  .back-brand .brand-name {
    display: block;
    font-size: 34px;
    letter-spacing: 2px;
    line-height: 1;
  }
  .back-brand .brand-tagline {
    display: block;
    font-size: 8.5px;
    margin-top: 4px;
    text-transform: uppercase;
  }

  .service-list {
    position: absolute;
    right: 50px; top: 46px;
    list-style: none;
    text-align: right;
    color: var(--white);
    font-size: 16px;
    line-height: 22.5px;
  }
  .service-list li { position: relative; padding-right: 20px; }
  .service-list li::after {
    content: "";
    position: absolute;
    right: 0; top: 7px;
    width: 10px; height: 10px;
    background: var(--orange);
    clip-path: polygon(50% 0, 100% 38%, 82% 100%, 18% 100%, 0 38%);
  }

  .employee-name {
    position: absolute;
    right: 38px; top: 161px;
    color: var(--orange);
    font-size: 23px;
    font-weight: 700;
  }

  .contact-row {
    position: absolute;
    right: 46px;
    width: 250px;
    display: flex;
    align-items: center;
    justify-content: flex-end;
    gap: 8px;
  }
  .contact-row.phone { top: 234px; }
  .contact-row.web { top: 280px; }
  .contact-lines {
    text-align: right;
    color: var(--white);
    font-size: 11.5px;
    line-height: 14px;
  }
  .contact-lines span { display: block; }
  .contact-lines span:first-child {
    border-bottom: 1px solid var(--rule);
    padding-bottom: 1px;
    margin-bottom: 1px;
  }
  .contact-icon { width: 34px; height: 32px; flex: none; }
</style>
</head>
<body>

  <!-- Front -->
  <section class="card-front" aria-label="Business card front">
    <svg class="bands" viewBox="0 0 777 444" width="777" height="444" aria-hidden="true">
      <defs>
        <linearGradient id="bandTop" x1="0" y1="0" x2="1" y2="0">
          <stop offset="0" stop-color="#c7320c"/>
          <stop offset="1" stop-color="#d94a1a"/>
        </linearGradient>
        <linearGradient id="bandBottom" x1="0" y1="0" x2="1" y2="0">
          <stop offset="0" stop-color="#c9340d"/>
          <stop offset="1" stop-color="#e0501d"/>
        </linearGradient>
      </defs>
      <polygon points="0,0 777,0 777,50 0,120" fill="url(#bandTop)"/>
      <polygon points="0,120 777,50 777,62 0,132" fill="#f26a2e"/>
      <polygon points="0,405 777,322 777,444 0,444" fill="url(#bandBottom)"/>
      <polygon points="0,405 777,322 777,333 0,416" fill="#f26a2e"/>
    </svg>
    <div class="front-brand">
      <span class="brand-name">CREST</span>
      <span class="brand-tagline">Automotive Reconditioning</span>
    </div>
  </section>

  <!-- Back -->
  <section class="card-back" aria-label="Business card back">
    <svg class="panels" viewBox="0 0 598 358" width="598" height="358" aria-hidden="true">
      <rect x="140" y="0" width="458" height="9" fill="var(--orange)"/>
      <rect x="110" y="350" width="488" height="8" fill="var(--orange)"/>
      <polygon points="140,0 160,0 245,148 160,358 110,358 222,148" fill="#d0d0d0"/>
      <polygon points="0,0 140,0 238,148 140,358 0,358" fill="var(--orange)"/>
    </svg>

    <div class="back-brand">
      <span class="brand-name">CREST</span>
      <span class="brand-tagline">Automotive Reconditioning</span>
    </div>

    <ul class="service-list">
      <li>Clear Coat Scratch Repair</li>
      <li>Bumper Repair and Repainting</li>
      <li>Road Rash Repair</li>
      <li>Automotive Touch-Up</li>
    </ul>

    <p class="employee-name">YOUR NAME</p>

    <div class="contact-row phone">
      <div class="contact-lines">
        <span>+ 000 - 1234 - 5678</span>
        <span>+ 000 - 9876 - 5432</span>
      </div>
      <svg class="contact-icon" viewBox="0 0 34 32" aria-label="Phone">
        <polygon points="8,0 26,0 34,16 26,32 8,32 0,16" fill="var(--orange)"/>
        <path d="M10 12 q7 -5 14 0 v2 h-4 v-2 h-6 v2 h-4z" fill="#fff"/>
        <rect x="11" y="15" width="12" height="7" rx="1" fill="#fff"/>
      </svg>
    </div>

    <div class="contact-row web">
      <div class="contact-lines">
        <span>admin@crestauto.com</span>
        <span>crestautomotive.com</span>
      </div>
      <svg class="contact-icon" viewBox="0 0 34 32" aria-label="Website">
        <polygon points="8,0 26,0 34,16 26,32 8,32 0,16" fill="var(--orange)"/>
        <rect x="9" y="9" width="16" height="11" fill="none" stroke="#fff" stroke-width="2"/>
        <rect x="14" y="21" width="6" height="2" fill="#fff"/>
        <rect x="12" y="23" width="10" height="1.5" fill="#fff"/>
      </svg>
    </div>
  </section>

</body>
</html>
```